Tarvold Equipment requires a design to be used for stickers that will go on all new Excavators sold.

Design a sticker to include Tarvold Equipment, want to use current corporate colours (Black and Red) but also incorporate the colour of the excavators we are selling so sticker looks in place and not cheap. We are happy at looking at modernising the Tarvold Equipment logo particularly font or writing style to suit earthmoving equipment (strong, tough). Interested in new ideas so not necessarily your standard square or rectangle shape.
Text would be :
Sold and Serviced by
TARVOLD EQUIPMENT
SALES-PARTS-SERVICE-RENTALS
Ph 1300 47 82 16
www.tarvoldmachinery-example.com.au
Tarvold Equipment would be dominate and largest, then phone number and reducing font quite a lot for other items

Target Market(s)

Earthmoving - so modern and hard, strong look

Requirements
Must have
• All items of text

```html
<!DOCTYPE html>
<html lang="en">
<head>
<meta charset="utf-8">
<title>Tarvold Equipment – Excavator Stickers</title>
<link rel="stylesheet" href="https://fonts.googleapis.com/css2?family=Exo+2:wght@600;900&family=Tinos:wght@700&display=swap">
<style>
  :root {
    --backdrop: #1bb0bd;
    --sticker-white: #ffffff;
    --sticker-black: #231f20;
    --brand-red: #ed1c24;
  }
  html, body {
    margin: 0;
    padding: 0;
    width: 1200px;
    height: 1000px;
    overflow: hidden;
    background: var(--backdrop);
  }
  .canvas {
    display: block;
    width: 1200px;
    height: 1000px;
  }
  .sticker-base { fill: var(--sticker-white); }
  .frame { fill: var(--sticker-black); }
  .panel-white { fill: var(--sticker-white); }
  .tagline {
    font-family: "Tinos", "Times New Roman", serif;
    font-weight: 700;
    fill: var(--sticker-black);
  }
  .brand-name {
    font-family: "Exo 2", Arial, sans-serif;
    font-weight: 900;
    fill: var(--sticker-black);
  }
  .brand-mark { fill: var(--brand-red); }
  .services, .phone, .web {
    font-family: "Exo 2", Arial, sans-serif;
    font-weight: 600;
    fill: var(--sticker-white);
  }
  .web { letter-spacing: 1.5px; }
  .phone-icon { fill: var(--sticker-white); }
</style>
</head>
<body>
<svg class="canvas" viewBox="0 0 1200 1000" xmlns="http://www.w3.org/2000/svg" role="img" aria-label="Tarvold Equipment excavator sticker designs in two formats">
  <defs>
    <symbol id="icon-phone" viewBox="0 0 48 40">
      <path d="M4 14 C4 4 44 4 44 14 L44 17 L34 17 L33 12 C27 10 21 10 15 12 L14 17 L4 17 Z"/>
      <path d="M14 18 L18 14 L30 14 L34 18 L42 34 L42 38 L6 38 L6 34 Z"/>
      <circle cx="24" cy="27" r="6" fill="var(--sticker-black)"/>
      <circle cx="24" cy="27" r="2.5"/>
    </symbol>
  </defs>

  <!-- Square sticker -->
  <g class="sticker sticker--square">
    <rect class="sticker-base" x="258" y="95" width="684" height="517"/>
    <rect class="frame" x="276" y="113" width="648" height="482"/>
    <rect class="panel-white" x="290" y="128" width="620" height="232"/>
    <rect class="panel-white" x="418" y="113" width="362" height="15"/>
    <text class="tagline" x="599" y="133" text-anchor="middle" font-size="29">Sold and Serviced by</text>
    <text class="brand-name" x="305" y="250" font-size="112" textLength="585" lengthAdjust="spacingAndGlyphs">TARVOLD</text>
    <text class="brand-name" x="390" y="328" font-size="66" textLength="358" lengthAdjust="spacingAndGlyphs">EQUIPMENT</text>
    <rect class="brand-mark" x="762" y="280" width="46" height="46"/>
    <text class="services" x="600" y="420" text-anchor="middle" font-size="36" textLength="604" lengthAdjust="spacingAndGlyphs">SALES-PARTS-SERVICE-RENTALS</text>
    <use class="phone-icon" href="#icon-phone" x="388" y="458" width="52" height="44"/>
    <text class="phone" x="460" y="497" font-size="50" textLength="350" lengthAdjust="spacingAndGlyphs">1300 47 82 16</text>
    <text class="web" x="600" y="550" text-anchor="middle" font-size="24" textLength="470" lengthAdjust="spacingAndGlyphs">www.tarvoldmachinery-example.com.au</text>
  </g>

  <!-- Long sticker -->
  <g class="sticker sticker--long">
    <rect class="sticker-base" x="112" y="683" width="983" height="217"/>
    <rect class="frame" x="124" y="696" width="959" height="192"/>
    <polygon class="panel-white" points="136,709 588,709 638,797 588,876 136,876"/>
    <rect class="panel-white" x="232" y="696" width="265" height="13"/>
    <text class="tagline" x="363" y="712" text-anchor="middle" font-size="23">Sold and Serviced by</text>
    <text class="brand-name" x="150" y="797" font-size="84" textLength="430" lengthAdjust="spacingAndGlyphs">TARVOLD</text>
    <text class="brand-name" x="212" y="856" font-size="52" textLength="256" lengthAdjust="spacingAndGlyphs">EQUIPMENT</text>
    <rect class="brand-mark" x="482" y="820" width="36" height="36"/>
    <text class="services" x="848" y="748" text-anchor="middle" font-size="27" textLength="442" lengthAdjust="spacingAndGlyphs">SALES-PARTS-SERVICE-RENTALS</text>
    <use class="phone-icon" href="#icon-phone" x="692" y="780" width="40" height="34"/>
    <text class="phone" x="746" y="809" font-size="37" textLength="258" lengthAdjust="spacingAndGlyphs">1300 47 82 16</text>
    <text class="web" x="848" y="850" text-anchor="middle" font-size="19" textLength="346" lengthAdjust="spacingAndGlyphs">www.tarvoldmachinery-example.com.au</text>
  </g>
</svg>
</body>
</html>
```